Modern Business Card Design for Independent Urban Music Label

We need a card design for an independent urban music label called Copper Tide Records based in London. We develop and promote urban British music artists. We attend lots of high profile events with high profile industry people and want a card that comes across both on-brand and sophisticated, professional, trustworthy. I have attached our logo - please use the black and orange version in the upper left HOWEVER we are open to seeing other colors than the orange used though we want the shape of the logo to remain the same.

Info to please include:
Name
Position
Phone
Email
Website

Additional Info:
Twitter: @CopperTideRecsUK
Insta: @CopperTideRecs

Target Market(s)

Industry professionals and others artists

Industry/Entity Type

Business

Contact Information for Business Card

Info to please include:
Name
Position
Phone
Email
Website

Additional Info:
Twitter: @CopperTideRecsUK
Insta: @CopperTideRecs

Requirements
Must have
• Logo, company name
• Info to please include:
• Name
• Position
• Phone
• Email
• Website
Nice to have
• Twitter: @CopperTideRecsUK
• Insta: @CopperTideRecs
• If it can be done so that it doesn't look cluttered

```html
<!DOCTYPE html>
<html lang="en">
<head>
<meta charset="utf-8">
<title>Copper Tide Records – Business Card</title>
<link href="https://fonts.googleapis.com/css2?family=Lato:wght@400;700&display=swap" rel="stylesheet">
<style>
  :root {
    --backdrop: #ecebe8;
    --card-white: #fbfbfb;
    --card-grey: #8b8a8d;
    --ink: #3a3839;
    --ink-soft: #4a4849;
    --copper: #f2a068;
    --copper-line: #f6bf94;
  }
  * { box-sizing: border-box; margin: 0; padding: 0; }
  html, body {
    width: 1200px; height: 1023px; overflow: hidden;
    background: var(--backdrop);
    font-family: "Lato", sans-serif;
  }
  .canvas { position: relative; width: 1200px; height: 1023px; }
  .card {
    position: absolute; left: 210px; width: 780px; height: 446px;
    border-radius: 6px; overflow: hidden;
    box-shadow: 0 8px 24px rgba(0,0,0,.18);
  }
  .card--front { top: 52px; background: var(--card-white); }
  .card--back  { top: 525px; background: linear-gradient(160deg, #979699, var(--card-grey) 60%, #7d7c7f); }

  .swoop { position: absolute; inset: 0; width: 100%; height: 100%; }

  .brand {
    position: absolute; display: flex; align-items: center; gap: 12px;
    font-weight: 700; text-transform: uppercase; letter-spacing: 2px;
    color: var(--copper);
  }
  .brand__dot { width: 26px; height: 26px; border-radius: 50%; background: var(--ink); flex: none; }
  .card--front .brand { left: 40px; top: 206px; font-size: 17px; }

  .divider {
    position: absolute; left: 318px; top: 112px; width: 3px; height: 216px;
    background: var(--copper-line);
  }

  .identity { position: absolute; left: 346px; top: 96px; }
  .identity__name { font-weight: 700; font-size: 24px; color: var(--copper); }
  .identity__role { font-size: 17px; color: var(--ink); margin-top: 4px; }

  .contacts { position: absolute; left: 346px; top: 176px; list-style: none; }
  .contacts li {
    display: flex; align-items: center; gap: 12px;
    font-size: 17px; color: var(--ink); height: 30px;
  }
  .contacts svg { width: 18px; height: 18px; flex: none; }

  .card--back .brand {
    left: 0; right: 0; top: 186px; justify-content: center;
    font-size: 24px; letter-spacing: 3px;
  }
  .card--back .brand__dot { width: 32px; height: 32px; background: var(--ink); }
  .handle {
    position: absolute; left: 0; right: 0; top: 236px; text-align: center;
    font-size: 17px; color: var(--ink-soft);
  }
</style>
</head>
<body>
<main class="canvas">

  <section class="card card--front" aria-label="Business card front">
    <svg class="swoop" viewBox="0 0 780 446" aria-hidden="true">
      <path d="M688 0 Q560 223 640 446 L662 446 Q610 223 720 0 Z" fill="var(--ink)"/>
    </svg>

    <div class="brand"><span class="brand__dot"></span>Copper Tide Records</div>

    <div class="divider"></div>

    <div class="identity">
      <p class="identity__name">Marcus Hale</p>
      <p class="identity__role">Director</p>
    </div>

    <ul class="contacts">
      <li>
        <svg viewBox="0 0 18 18" aria-hidden="true"><rect width="18" height="18" rx="3" fill="var(--ink)"/><path d="M5 4h2.5l1 3-1.5 1a7 7 0 0 0 3 3l1-1.5 3 1V13a1 1 0 0 1-1 1A9 9 0 0 1 4 5a1 1 0 0 1 1-1z" fill="#fff"/></svg>
        020 7946 0321
      </li>
      <li>
        <svg viewBox="0 0 18 18" aria-hidden="true"><rect width="18" height="18" rx="3" fill="var(--ink)"/><rect x="3.5" y="5" width="11" height="8" fill="none" stroke="#fff" stroke-width="1.3"/><path d="M3.5 5 9 10l5.5-5" fill="none" stroke="#fff" stroke-width="1.3"/></svg>
        marcus@coppertide.co.uk
      </li>
      <li>
        <svg viewBox="0 0 18 18" aria-hidden="true"><circle cx="9" cy="9" r="8" fill="var(--ink)"/><g fill="none" stroke="#fff" stroke-width="1"><circle cx="9" cy="9" r="5.5"/><ellipse cx="9" cy="9" rx="2.3" ry="5.5"/><path d="M3.5 9h11"/></g></svg>
        www.coppertide.co.uk
      </li>
      <li>
        <svg viewBox="0 0 18 18" aria-hidden="true"><rect width="18" height="18" rx="3" fill="var(--ink)"/></svg>
        @CopperTideRecsUK
      </li>
      <li>
        <svg viewBox="0 0 18 18" aria-hidden="true"><rect width="18" height="18" rx="3" fill="var(--ink)"/></svg>
        @CopperTideRecs
      </li>
    </ul>
  </section>

  <section class="card card--back" aria-label="Business card back">
    <div class="brand"><span class="brand__dot"></span>Copper Tide Records</div>
    <p class="handle">@CopperTideRecsUK</p>
  </section>

</main>
</body>
</html>
```